GLOW AT NOON (EP) FOR KEMASO, AN ARTISTE SIGNED TO LANTERN ENTERTAINMENTS

A CREATIVELY SIMPLE EVERGREEN DESIGN. BECAUSE NO PICTURE IS REQUIRED, THE DESIGN HAS TO BE VERY EYE CATCHING AND COLOURFUL AND I WANT THE BEST CONCEPT TO DESCRIBE THE TITLE.

DETAILS TO BE USED ON THE DESIGN AS FOLLOWS

RECORDING LABEL: LANTERN ENTERTAINMENTS
ARTISTE NAME: KEMASO
EP TITLE: GLOW AT NOON
TRACK LIST
1. EKE DURADE (Produced by Zumol)
2. ROOFTOP PARADE (Produced by K.R.V Beats)
3. U SEF TAYE (PRODUCED BY B'KEYZ)
4. UNDER THE GOLDEN EVENING SUN (PRODUCED BY GRIMBO JAY)
5. RISE GLIDE SHINE (PRODUCED BY VELKU)

ALL SONGS MIXED BY ZEK MORROW.

Target Market(s)

AFRICA

Font styles to use
Serif
Sans Serif
Decorative
Script

Colors

Designer to choose colors to be used in the design.

Requirements
Must have
• A CREATIVELY SIMPLE EVERGREEN DESIGN
Nice to have
Should not have
• NON

```html
<!DOCTYPE html>
<html lang="en">
<head>
<meta charset="utf-8">
<title>KEMASO – GLOW AT NOON</title>
<link rel="stylesheet" href="https://fonts.googleapis.com/css2?family=Barlow+Condensed:wght@700&display=swap">
<style>
  :root {
    --ink-white: #ffffff;
    --electric-blue: #3a3fd6;
    --violet: #6a3ad0;
    --warm-orange: #d98a4a;
    --mint: #a6e2d6;
    --magenta: #b84ad6;
    --turquoise: #22d4cc;
    --label-dark: #0b0b0b;
  }
  html, body {
    margin: 0;
    padding: 0;
    width: 1200px;
    height: 1200px;
    overflow: hidden;
    background: #ffffff;
  }
  .cover {
    position: relative;
    width: 1200px;
    height: 1200px;
    overflow: hidden;
    font-family: "Barlow Condensed", "Oswald", sans-serif;
    color: var(--ink-white);
  }
  .colour-field {
    position: absolute;
    inset: 0;
    background: linear-gradient(115deg,
      var(--electric-blue) 0%,
      var(--violet) 25%,
      var(--warm-orange) 45%,
      var(--mint) 65%,
      var(--magenta) 85%,
      var(--turquoise) 100%);
  }
  .artist-name {
    position: absolute;
    left: 76px;
    top: 38px;
    margin: 0;
    font-size: 246px;
    line-height: 1;
    font-weight: 700;
    letter-spacing: -4px;
  }
  .ep-title {
    position: absolute;
    right: 82px;
    top: 724px;
    margin: 0;
    text-align: right;
    font-size: 168px;
    line-height: 134px;
    font-weight: 700;
    letter-spacing: -1px;
  }
  .ep-title span { display: block; }
  .label-mark {
    position: absolute;
    left: 80px;
    top: 1070px;
    display: flex;
    align-items: center;
    gap: 10px;
    font-size: 20px;
    line-height: 1.05;
    font-weight: 700;
    letter-spacing: 0.5px;
  }
  .label-square {
    width: 40px;
    height: 40px;
    background: var(--label-dark);
  }
</style>
</head>
<body>
  <main class="cover">
    <div class="colour-field" role="img" aria-label="Abstract flowing liquid paint artwork in blue, violet, orange, mint and magenta"></div>
    <h1 class="artist-name">KEMASO</h1>
    <h2 class="ep-title"><span>GLOW</span><span>AT</span><span>NOON</span></h2>
    <div class="label-mark">
      <div class="label-square"></div>
      <div class="label-name">LANTERN<br>ENTERTAINMENTS</div>
    </div>
  </main>
</body>
</html>
```